Business Card Design (NEW FILES)

ATTENTION: New vector files are available. Please update your design to reflect/use the new (better resolution) logo images.

Seeking a unique and professional business card design for a commercial drone photography/videography business. The layout should feature
the logo (attached) and include the following information:
978-512-6037
www.skyvantmedia.com
ORD Certified Remote Pilot

```html
<!DOCTYPE html>
<html lang="en">
<head>
<meta charset="utf-8">
<title>Skyvant Media — Business Card</title>
<link rel="stylesheet" href="https://fonts.googleapis.com/css2?family=Montserrat:wght@400;500;600&family=Lato:wght@400;700&display=swap">
<style>
  :root {
    --page-bg: #0f1444;
    --navy: #1d1d62;
    --navy-deep: #15164d;
    --orange: #e8904f;
    --paper: #f4f4f6;
    --ink: #1d1d62;
    --muted-line: #8a8aa8;
    --text-dark: #2b2b3a;
  }
  * { margin: 0; padding: 0; box-sizing: border-box; }
  html, body { width: 1200px; height: 1200px; overflow: hidden; }
  body {
    background: var(--page-bg);
    font-family: "Lato", sans-serif;
    position: relative;
  }
  .card {
    position: absolute;
    left: 220px;
    width: 760px;
    height: 434px;
    border-radius: 4px;
    overflow: hidden;
    box-shadow: 0 20px 50px rgba(0,0,0,0.45);
  }
  .card--front { top: 150px; background: linear-gradient(160deg, var(--navy) 0%, var(--navy-deep) 100%); }
  .card--back { top: 620px; background: var(--paper); }
  .card-bands { position: absolute; inset: 0; width: 100%; height: 100%; }

  .brand {
    position: absolute;
    display: flex;
    align-items: center;
    gap: 14px;
    font-family: "Montserrat", sans-serif;
    font-weight: 500;
    font-size: 40px;
    letter-spacing: 3px;
    text-transform: uppercase;
    white-space: nowrap;
  }
  .brand-dot { width: 26px; height: 26px; border-radius: 50%; background: var(--orange); flex: none; }
  .card--front .brand { left: 0; right: 0; top: 130px; justify-content: center; color: #ffffff; }
  .card--back .brand { left: 44px; top: 150px; color: var(--ink); font-size: 32px; gap: 12px; }
  .card--back .brand-dot { width: 22px; height: 22px; }

  .credentials {
    position: absolute;
    display: flex;
    align-items: center;
    gap: 18px;
    font-family: "Montserrat", sans-serif;
    font-size: 15px;
    letter-spacing: 3px;
    text-align: center;
    line-height: 1.6;
  }
  .credentials .rule { height: 1px; flex: 1; }
  .card--front .credentials { left: 100px; right: 100px; top: 225px; color: #b9b9d6; }
  .card--front .credentials .rule { background: var(--muted-line); }
  .card--back .credentials { left: 30px; width: 400px; top: 222px; color: var(--text-dark); font-size: 13px; letter-spacing: 2.5px; }
  .card--back .credentials .rule { background: #55556a; }

  .contact { position: absolute; left: 470px; top: 70px; width: 260px; }
  .contact-name {
    font-family: "Montserrat", sans-serif;
    font-weight: 600;
    font-size: 28px;
    color: var(--ink);
    text-transform: uppercase;
    letter-spacing: 0.5px;
  }
  .contact-role { font-size: 22px; color: var(--orange); margin-top: 2px; }
  .contact-rule { height: 1px; background: var(--orange); margin: 10px 0 18px; }
  .contact-list { list-style: none; }
  .contact-list li { display: flex; align-items: flex-start; gap: 14px; margin-bottom: 14px; font-size: 15px; color: var(--text-dark); line-height: 1.3; }
  .icon { width: 26px; height: 26px; flex: none; display: flex; align-items: center; justify-content: center; background: var(--navy); }
  .icon--accent { background: var(--orange); }
  .icon svg { width: 16px; height: 16px; }
</style>
</head>
<body>

<section class="card card--front" aria-label="Card front">
  <svg class="card-bands" viewBox="0 0 760 434" preserveAspectRatio="none" aria-hidden="true">
    <polygon points="0,422 470,422 490,392 760,392 760,434 0,434" fill="var(--orange)"/>
  </svg>
  <div class="brand"><span class="brand-dot"></span>Skyvant Media</div>
  <div class="credentials">
    <span class="rule"></span>
    <p>ORD Certified Remote Pilot<br>Fully Insured</p>
    <span class="rule"></span>
  </div>
</section>

<section class="card card--back" aria-label="Card back">
  <svg class="card-bands" viewBox="0 0 760 434" preserveAspectRatio="none" aria-hidden="true">
    <polygon points="0,390 420,390 400,434 0,434" fill="var(--navy)"/>
    <polygon points="440,360 760,360 760,434 420,434" fill="var(--orange)"/>
  </svg>
  <div class="brand"><span class="brand-dot"></span>Skyvant Media</div>
  <div class="credentials">
    <span class="rule"></span>
    <p>ORD Certified Remote Pilot<br>Fully Insured</p>
    <span class="rule"></span>
  </div>

  <div class="contact">
    <h1 class="contact-name">Mark Doyle</h1>
    <p class="contact-role">Owner</p>
    <div class="contact-rule"></div>
    <ul class="contact-list">
      <li>
        <span class="icon"><svg viewBox="0 0 24 24" fill="#fff"><path d="M6.6 10.8a15.1 15.1 0 0 0 6.6 6.6l2.2-2.2c.3-.3.7-.4 1-.2 1.1.4 2.3.6 3.6.6.6 0 1 .4 1 1V20c0 .6-.4 1-1 1A17 17 0 0 1 3 4c0-.6.4-1 1-1h3.5c.6 0 1 .4 1 1 0 1.3.2 2.5.6 3.6.1.3 0 .7-.2 1z"/></svg></span>
        <span>978-512-6037</span>
      </li>
      <li>
        <span class="icon"><svg viewBox="0 0 24 24" fill="#fff"><path d="M5 3l14 7-6 2-2 6z"/></svg></span>
        <span>www.skyvantmedia.com</span>
      </li>
      <li>
        <span class="icon icon--accent"><svg viewBox="0 0 24 24" fill="#fff"><path d="M12 2a7 7 0 0 0-7 7c0 5 7 13 7 13s7-8 7-13a7 7 0 0 0-7-7zm0 9.5A2.5 2.5 0 1 1 12 6.5a2.5 2.5 0 0 1 0 5z"/></svg></span>
        <span>2170 Harbor Ridge Avenue<br>Arlington, VA 22201</span>
      </li>
    </ul>
  </div>
</section>

</body>
</html>
```